Labels for Hair care products
Labels for hair care products
Project: Labels for Hair care products
Labels for Hair care products  - Salon & Spa
Creative Brief
im looking for new label designs for my hair products i will supply my logo,artwork from my pervious labels and descriptions for each product company name is: QR Scalp Works product line name is called: Grit Rebel
Salon & Spa
lets make it rough and tough looking my demographic target is age 8-30
please make sure i can edit the text, send me all files you use for each label so that i don't have any errors when opening into adobe illustrator. lets keep it about 4 to 5 color max make sure that each label clearly shows that its Shampoo, conditioner, etc

```html
<!DOCTYPE html>
<html lang="en">
<head>
<meta charset="utf-8">
<title>QR Scalp Works – Grit Rebel Conditioner Labels</title>
<link href="https://fonts.googleapis.com/css2?family=Racing+Sans+One&family=Roboto+Condensed:wght@400;700&display=swap" rel="stylesheet">
<style>
  :root {
    --stage: #2b2d30;
    --label-black: #111213;
    --label-grey: #2a2c2e;
    --lime: #8dc63f;
    --lime-bright: #a6e04a;
    --white: #ffffff;
    --soft-grey: #b9bcbf;
    --caption: #e4e6e8;
  }
  * { box-sizing: border-box; margin: 0; padding: 0; }
  html, body { width: 1200px; height: 926px; overflow: hidden; }
  body {
    background: var(--stage);
    font-family: "Roboto Condensed", Arial, sans-serif;
    color: var(--white);
    position: relative;
  }
  .brand-title {
    position: absolute; top: 50px; left: 0; width: 1200px;
    text-align: center;
    font-family: "Racing Sans One", Impact, sans-serif;
    font-size: 72px; color: var(--lime); letter-spacing: 1px;
  }
  .label {
    position: absolute; top: 190px; width: 400px; height: 520px;
    background: linear-gradient(180deg, var(--label-grey) 0%, var(--label-black) 55%, var(--label-grey) 100%);
    overflow: hidden;
  }
  .label--back { left: 170px; }
  .label--front { left: 630px; }

  .product-name {
    font-family: "Racing Sans One", Impact, sans-serif;
    line-height: 0.95;
  }
  .product-name .line-name { display: block; color: var(--lime); }
  .product-name .line-type { display: block; color: var(--white); }

  /* back label */
  .label--back .product-name { position: absolute; top: 26px; left: 30px; }
  .label--back .line-name { font-size: 34px; }
  .label--back .line-type { font-size: 46px; }
  .info-panel {
    position: absolute; top: 136px; left: 30px; width: 340px; height: 300px;
    background: var(--white); border: 4px solid var(--lime);
    border-radius: 6px; color: #222; padding: 22px 22px 14px;
  }
  .info-copy { font-size: 14.5px; line-height: 1.45; }
  .info-footer {
    position: absolute; left: 22px; right: 22px; bottom: 14px;
    display: flex; justify-content: space-between; align-items: flex-end;
  }
  .info-brand {
    font-family: "Racing Sans One", Impact, sans-serif;
    font-size: 22px; color: var(--lime); line-height: 1;
  }
  .info-contact { font-size: 10.5px; line-height: 1.4; text-align: left; color: #333; }
  .web {
    position: absolute; bottom: 40px; left: 0; width: 100%;
    text-align: center; font-weight: 700; font-size: 18px; color: var(--lime);
  }

  /* front label */
  .made-in {
    position: absolute; top: 20px; right: 28px;
    font-size: 13px; font-weight: 700; letter-spacing: 1px; color: var(--white);
  }
  .front-brand {
    position: absolute; top: 44px; left: 30px;
    font-family: "Racing Sans One", Impact, sans-serif;
    font-size: 40px; color: var(--lime); line-height: 1;
  }
  .audience {
    position: absolute; top: 96px; left: 30px;
    font-size: 17px; font-weight: 700; letter-spacing: 1px; color: var(--lime-bright);
  }
  .rider-photo {
    position: absolute; top: 140px; left: 0; width: 400px; height: 230px;
    display: block;
  }
  .label--front .product-name { position: absolute; bottom: 46px; right: 28px; text-align: right; }
  .label--front .line-name { font-size: 38px; }
  .label--front .line-type { font-size: 50px; }
  .volume {
    position: absolute; bottom: 18px; right: 28px;
    font-size: 12px; font-weight: 700; color: var(--soft-grey);
  }

  .caption {
    position: absolute; top: 740px; width: 400px; text-align: center;
    font-size: 20px; color: var(--caption);
  }
  .caption--back { left: 170px; }
  .caption--front { left: 630px; }
</style>
</head>
<body>
  <h1 class="brand-title">QR Scalp Works</h1>

  <section class="label label--back" aria-label="Back label">
    <div class="product-name">
      <span class="line-name">GRIT REBEL</span>
      <span class="line-type">Conditioner</span>
    </div>
    <div class="info-panel">
      <p class="info-copy">No one likes having Helmet Hair, and our specially formulated Grit Rebel Conditioner is designed to be lightweight, for detangling that won't weigh your hair down. Made for normal to oily hair, Vitamins A and E moisturize and soften the cuticle, so no matter how hard you ride, your hair will always be smooth.</p>
      <div class="info-footer">
        <span class="info-brand">QR Scalp Works</span>
        <p class="info-contact">QR Scalp Works<br>4120 Ridgeline Ave<br>Fernvale, CA 90000<br>(555) 204-7719<br>info@qrscalpworks.com</p>
      </div>
    </div>
    <p class="web">qrscalpworks.com</p>
  </section>

  <section class="label label--front" aria-label="Front label">
    <p class="made-in">MADE IN U.S.A.</p>
    <p class="front-brand">QR Scalp Works</p>
    <p class="audience">FOR MEN OR WOMEN</p>
    <svg class="rider-photo" viewBox="0 0 400 230" role="img" aria-label="Black and white photo of a motocross rider on a dirt bike">
      <defs>
        <radialGradient id="riderTone" cx="50%" cy="50%" r="60%">
          <stop offset="0%" stop-color="#6b6e71"/>
          <stop offset="60%" stop-color="#35383a"/>
          <stop offset="100%" stop-color="#151617" stop-opacity="0"/>
        </radialGradient>
      </defs>
      <rect width="400" height="230" fill="url(#riderTone)"/>
    </svg>
    <div class="product-name">
      <span class="line-name">GRIT REBEL</span>
      <span class="line-type">Conditioner</span>
    </div>
    <p class="volume">16 fl oz 473 ml</p>
  </section>

  <p class="caption caption--back">Label BACK</p>
  <p class="caption caption--front">Label FRONT</p>
</body>
</html>
```